Wavelume artwork for new single release

I need Wavelume artwork creating to release a new single on there.

The specs are:

Ideal size: 3000 x 3000 pixels
Minimum size: 1400 x 1400 pixels
Aspect ratio: 1:1 (must be a perfect square)
File format: JPG or PNG
Color space: sRGB
File size: Max 4MB

The song is called "Still, Can We Wander?"
The artist is "Milo Fenwright"

We have no images of Milo, so it really is open to imagination.

Target Market(s)

Wavelume listeners

Industry/Entity Type

Music

```html
<!DOCTYPE html>
<html lang="en">
<head>
<meta charset="utf-8">
<title>Still, Can We Wander? — Milo Fenwright</title>
<link href="https://fonts.googleapis.com/css2?family=Montserrat:ital,wght@1,800&family=Great+Vibes&family=Poppins:wght@400;500;600&display=swap" rel="stylesheet">
<style>
  :root {
    --bg: #0b0b0c;
    --white: #ffffff;
    --muted: #b9b9bd;
    --track: #5a5a5e;
    --magenta: #d2298f;
    --violet: #7a2fb8;
    --plum: #3a1b55;
    --rose: #f06bb8;
  }
  * { margin: 0; padding: 0; box-sizing: border-box; }
  html, body { width: 720px; height: 1200px; overflow: hidden; background: var(--bg); }
  .player {
    position: relative; width: 720px; height: 1200px; overflow: hidden;
    background: var(--bg); font-family: "Poppins", sans-serif; color: var(--white);
  }
  .backdrop {
    position: absolute; left: 0; top: 0; width: 720px; height: 760px;
    background:
      linear-gradient(180deg, transparent 0%, transparent 78%, var(--bg) 100%),
      radial-gradient(ellipse 260px 420px at 80px 330px, rgba(210,41,143,0.6), transparent 70%),
      radial-gradient(ellipse 300px 220px at 520px 120px, rgba(240,107,184,0.55), transparent 70%),
      radial-gradient(ellipse 260px 300px at 680px 260px, rgba(122,47,184,0.55), transparent 70%),
      linear-gradient(180deg, #4a1f5e 0%, #3a1848 55%, #1a0f1e 100%);
  }
  .artwork {
    position: absolute; left: 82px; top: 173px; width: 559px; height: 559px; overflow: hidden;
    box-shadow: 0 10px 30px rgba(0,0,0,0.45);
    background:
      radial-gradient(ellipse 150px 220px at 290px 130px, rgba(255,170,220,0.5), transparent 70%),
      radial-gradient(ellipse 220px 180px at 470px 60px, rgba(240,107,184,0.75), transparent 70%),
      radial-gradient(ellipse 200px 280px at 40px 160px, rgba(210,41,143,0.8), transparent 70%),
      radial-gradient(ellipse 300px 220px at 300px 480px, rgba(122,47,184,0.75), transparent 70%),
      linear-gradient(180deg, #6a2a8e 0%, var(--violet) 40%, var(--magenta) 72%, var(--plum) 100%);
  }
  .artwork-title {
    position: absolute; right: 26px; top: 312px; text-align: right; font-weight: normal;
    text-shadow: 0 4px 14px rgba(40,0,40,0.55);
  }
  .artwork-title .lead {
    display: block; font-family: "Montserrat", sans-serif; font-style: italic; font-weight: 800;
    font-size: 54px; line-height: 1; letter-spacing: -1px;
  }
  .artwork-title .script {
    display: block; font-family: "Great Vibes", cursive; font-size: 80px; line-height: 1.05;
    margin-top: 0;
  }
  .artwork-title .byline {
    display: block; font-size: 19px; font-weight: 500; margin-top: 4px; margin-right: 54px;
  }
  .track-info { position: absolute; left: 0; top: 786px; width: 720px; text-align: center; }
  .track-title { font-size: 31px; font-weight: 600; line-height: 1.2; }
  .track-artist { font-size: 25px; color: var(--muted); margin-top: 6px; }
  .progress { position: absolute; left: 0; top: 920px; width: 720px; height: 34px; }
  .time { position: absolute; top: 2px; font-size: 19px; color: var(--white); }
  .time.elapsed { left: 96px; }
  .time.total { left: 574px; }
  .bar { position: absolute; left: 156px; top: 15px; width: 408px; height: 4px; border-radius: 2px; background: var(--track); }
  .bar-fill { position: absolute; left: 0; top: 0; width: 108px; height: 4px; border-radius: 2px; background: var(--white); }
  .bar-knob { position: absolute; left: 98px; top: -6px; width: 16px; height: 16px; border-radius: 50%; background: var(--white); }
  .controls { position: absolute; left: 0; top: 966px; width: 720px; height: 108px; }
  .controls svg { position: absolute; }
</style>
</head>
<body>
<main class="player">
  <div class="backdrop" role="img" aria-label="Blurred enlargement of the cover art in magenta and violet tones"></div>
  <section class="artwork" role="img" aria-label="Square cover art: a couple embracing in a dreamy magenta and violet haze beside a soft profile silhouette and scattered rose petals">
    <h1 class="artwork-title">
      <span class="lead">Still, Can We</span>
      <span class="script">Wander?</span>
      <span class="byline">By Milo Fenwright</span>
    </h1>
  </section>

  <div class="track-info">
    <p class="track-title">Still, can we wander?</p>
    <p class="track-artist">Milo Fenwright</p>
  </div>

  <div class="progress">
    <span class="time elapsed">1.04</span>
    <div class="bar"><div class="bar-fill"></div><div class="bar-knob"></div></div>
    <span class="time total">4.23</span>
  </div>

  <div class="controls">
    <svg class="icon-repeat" style="left:126px;top:36px" width="36" height="36" viewBox="0 0 36 36" fill="none" stroke="#fff" stroke-width="3" stroke-linecap="round" stroke-linejoin="round">
      <path d="M7 16 A11 11 0 0 1 27 11"/><path d="M27 5 V11 H21"/>
      <path d="M29 20 A11 11 0 0 1 9 25"/><path d="M9 31 V25 H15"/>
    </svg>
    <svg class="icon-prev" style="left:206px;top:28px" width="52" height="52" viewBox="0 0 52 52" fill="none" stroke="#fff" stroke-width="3">
      <circle cx="26" cy="26" r="24"/>
      <path d="M31 17 L20 26 L31 35 Z" fill="#fff" stroke="none"/>
      <rect x="17" y="17" width="3" height="18" fill="#fff" stroke="none"/>
    </svg>
    <svg class="icon-play" style="left:307px;top:0" width="106" height="106" viewBox="0 0 106 106">
      <circle cx="53" cy="53" r="53" fill="#fff"/>
      <rect x="40" y="35" width="8" height="36" rx="2" fill="#0b0b0c"/>
      <rect x="58" y="35" width="8" height="36" rx="2" fill="#0b0b0c"/>
    </svg>
    <svg class="icon-next" style="left:459px;top:28px" width="52" height="52" viewBox="0 0 52 52" fill="none" stroke="#fff" stroke-width="3">
      <circle cx="26" cy="26" r="24"/>
      <path d="M21 17 L32 26 L21 35 Z" fill="#fff" stroke="none"/>
      <rect x="32" y="17" width="3" height="18" fill="#fff" stroke="none"/>
    </svg>
    <svg class="icon-queue" style="left:566px;top:38px" width="36" height="32" viewBox="0 0 36 32" fill="none" stroke="#fff" stroke-width="3" stroke-linecap="round">
      <path d="M3 5 H18"/><path d="M3 13 H18"/><path d="M3 21 H12"/>
      <path d="M26 24 V5 L33 8"/><circle cx="22" cy="25" r="4" fill="#fff" stroke="none"/>
    </svg>
  </div>
</main>
</body>
</html>
```